New Optometry Practice needs a Business Card

Need a business card for an Optometry practice called 'Marlow Family Eyecare'. I would like to use designs that are friendly, fun and professional. Looking to incorporate glasses (see uploaded image). Not interested in design with an 'eye' in logo. Like green, blue, white as color choices..but open to your ideas. Back of card will be an appointment card as well as provide address, phone and email information.

Industry/Entity Type

Business

Contact Information for Business Card

Marlow Family Eyecare
Dr. Celeste Varga, Optometrist (or O.D.)
4170 S Brackenridge Rd Wenatchee, WA 98802
CMarlowfamilyeyecare.example

Colors
acd036
33b8a4
f68d4e
cfeae6
fee18a
cadf82

Requirements
Must have
• Appointment card on back with date/time of return for next exam

```html
<!DOCTYPE html>
<html lang="en">
<head>
<meta charset="utf-8">
<title>Marlow Family Eyecare – Business Card</title>
<link href="https://fonts.googleapis.com/css2?family=Open+Sans:wght@400;600;700&display=swap" rel="stylesheet">
<style>
  :root {
    --bg: #e9e6e1;
    --card-dark: #222526;
    --card-dark-2: #3b3f40;
    --teal: #33b8a4;
    --teal-edge: #2a9d8d;
    --white: #ffffff;
    --ink: #2b2b2b;
    --rule: #555555;
    --paper: #f7f7f7;
    --band: #1e1f20;
  }
  * { box-sizing: border-box; margin: 0; padding: 0; }
  html, body { width: 1200px; height: 1023px; overflow: hidden; }
  body {
    background: var(--bg);
    font-family: "Open Sans", Arial, sans-serif;
    position: relative;
  }
  .card {
    position: absolute;
    width: 620px;
    height: 354px;
    border-radius: 4px;
    overflow: hidden;
    box-shadow: 0 10px 30px rgba(0,0,0,.18);
  }

  /* Front */
  .card-front {
    left: 70px; top: 100px;
    background: linear-gradient(135deg, var(--card-dark) 0%, var(--card-dark-2) 55%, var(--card-dark) 100%);
    border-right: 10px solid var(--teal-edge);
    color: var(--white);
  }
  .brand {
    position: absolute; left: 34px; top: 92px; width: 296px;
  }
  .brand-rule { height: 3px; background: var(--teal); }
  .brand-rule.top { width: 246px; margin-left: 50px; }
  .brand-name {
    display: flex; align-items: center; gap: 9px;
    color: var(--teal); font-weight: 700; font-size: 23px;
    padding: 10px 0 8px 4px; white-space: nowrap;
  }
  .brand-dot { width: 11px; height: 11px; border-radius: 50%; background: var(--teal); flex: none; }
  .doctor { position: absolute; left: 96px; top: 232px; }
  .doctor-name { color: var(--teal); font-weight: 700; font-size: 19px; }
  .doctor-title { font-size: 14px; margin-top: 4px; }
  .divider {
    position: absolute; left: 352px; top: 112px; width: 1px; height: 140px;
    background: linear-gradient(transparent, rgba(51,184,164,.6), transparent);
  }
  .front-contact {
    position: absolute; left: 368px; top: 140px;
    font-size: 13px; line-height: 1.65; white-space: nowrap;
  }
  .web-line { display: flex; align-items: center; gap: 6px; }

  /* Back */
  .card-back {
    left: 510px; top: 560px;
    background: linear-gradient(160deg, var(--white), var(--paper));
    color: var(--ink);
  }
  .appointment { position: absolute; left: 34px; top: 28px; }
  .label { font-weight: 700; font-size: 14px; letter-spacing: .3px; }
  .appt-row { display: flex; gap: 10px; font-size: 13px; margin-top: 10px; align-items: flex-end; }
  .blank { display: inline-block; border-bottom: 1px solid var(--rule); height: 1px; }
  .blank.date { width: 110px; }
  .blank.time { width: 52px; }
  .practice { position: absolute; left: 34px; top: 150px; font-size: 13px; line-height: 1.5; }
  .practice-name { color: var(--teal); font-weight: 700; }
  .phone-line { display: flex; align-items: center; gap: 6px; }
  .hours-divider { position: absolute; left: 318px; top: 30px; width: 1px; height: 110px; background: #9a9a9a; }
  .hours { position: absolute; left: 338px; top: 30px; font-size: 13px; line-height: 1.55; }
  .back-band {
    position: absolute; left: 0; bottom: 0; width: 100%; height: 40px;
    background: var(--band); color: var(--white);
    font-size: 13px; display: flex; align-items: center; padding-left: 34px;
  }
  .motif {
    position: absolute; right: 0; bottom: 0; width: 200px; height: 150px;
    background: radial-gradient(circle at 70% 70%, #cfcfcf, #e9e9e9 60%, var(--paper));
  }
</style>
</head>
<body>

  <section class="card card-front" aria-label="Business card front">
    <div class="brand">
      <div class="brand-rule top"></div>
      <div class="brand-name"><span class="brand-dot"></span>Marlow Family Eyecare</div>
      <div class="brand-rule"></div>
    </div>
    <div class="doctor">
      <div class="doctor-name">Dr. Celeste Varga</div>
      <div class="doctor-title">Optometrist (or O.D.)</div>
    </div>
    <div class="divider"></div>
    <div class="front-contact">
      <div>4170 S Brackenridge Rd</div>
      <div>Wenatchee, WA 98802</div>
      <div class="web-line">
        <svg width="13" height="13" viewBox="0 0 14 14" aria-hidden="true"><circle cx="7" cy="7" r="6" fill="var(--teal)"/><path d="M1 7h12M7 1c-3 3-3 9 0 12M7 1c3 3 3 9 0 12" stroke="#222" stroke-width="1" fill="none"/></svg>
        CMarlowfamilyeyecare.example
      </div>
    </div>
  </section>

  <section class="card card-back" aria-label="Business card back">
    <div class="appointment">
      <div class="label">APPOINTMENT:</div>
      <div class="appt-row"><span>Date</span><span class="blank date"></span><span>Time</span><span class="blank time"></span></div>
      <div class="appt-row"><span>Date</span><span class="blank date"></span><span>Time</span><span class="blank time"></span></div>
      <div class="appt-row"><span>Date</span><span class="blank date"></span><span>Time</span><span class="blank time"></span></div>
    </div>
    <div class="practice">
      <div class="practice-name">Marlow Family Eyecare</div>
      <div>4170 S Brackenridge Rd</div>
      <div>Wenatchee, WA 98802</div>
      <div class="phone-line">
        <svg width="11" height="11" viewBox="0 0 12 12" aria-hidden="true"><circle cx="6" cy="6" r="6" fill="var(--ink)"/><path d="M4 3.2l1 1.3-.6.8c.5 1 1.2 1.7 2.2 2.2l.8-.6 1.3 1-.7 1C5.8 8.8 3.2 6.2 3 4z" fill="#fff"/></svg>
        07700 900 482
      </div>
      <div class="phone-line">
        <svg width="11" height="11" viewBox="0 0 12 12" aria-hidden="true"><circle cx="6" cy="6" r="6" fill="var(--ink)"/><path d="M4 3.2l1 1.3-.6.8c.5 1 1.2 1.7 2.2 2.2l.8-.6 1.3 1-.7 1C5.8 8.8 3.2 6.2 3 4z" fill="#fff"/></svg>
        01632 960 275
      </div>
      <div>celestevarga@CMarlowfamilyeyecare.example</div>
    </div>
    <div class="hours-divider"></div>
    <div class="hours">
      <div class="label">OFFICE HOURS:</div>
      <div>Monday - Wednesday:</div>
      <div>9 am - 1 pm, 3 pm - 5 pm</div>
      <div>Thursday: 9 am - 1 pm, 3 pm - 6 pm</div>
    </div>
    <div class="back-band">CMarlowfamilyeyecare.example</div>
    <div class="motif" role="img" aria-label="Decorative circle motif in grey, teal, green and yellow"></div>
  </section>

</body>
</html>
```